New custom software business needs a Wordpress site

We need a Wordpress site for a new company based out of Chicago called 'Vellora Consulting'. Using a mix of on and off-shore resources we build custom software solutions, mainly focusing on small to medium sized companies. We help our customers "aspire" to do great things.
We have a basic site up here: https://brindlewave.example/. We worked on the content for it but not the branding. For now, this houses all the pages (except for a Contact Us page we'll be adding soon) for the foreseeable future.
We also have a new logo (attached) that we'd like to base the styling/colors on.
Target Market(s)
Small to medium sized companies that require tech resources
Industry/Entity Type
Software
Nice to have
- Teamwork, tech, professional but not elitist

```html
<!DOCTYPE html>
<html lang="en">
<head>
<meta charset="utf-8">
<title>Vellora Consulting</title>
<link href="https://fonts.googleapis.com/css2?family=Poppins:wght@300;400;500;600;700;800&display=swap" rel="stylesheet">
<style>
:root{
  --blue:#1a62b4;
  --blue-dark:#0f3f86;
  --navy:#101c5c;
  --ink:#1b1b1b;
  --text:#333;
  --muted:#8a8a8a;
  --grey-bg:#f6f6f6;
  --footer:#4a8cc7;
  --news:#93b9e2;
  --white:#fff;
}
*{box-sizing:border-box;margin:0;padding:0}
html,body{width:1200px;height:2862px;overflow:hidden}
body{font-family:'Poppins',sans-serif;color:var(--text);background:#fff;position:relative}
.abs{position:absolute}
.topbar{left:0;top:0;width:1200px;height:33px;background:var(--blue);color:#fff;font-size:9px;display:flex;align-items:center}
.topbar .item{position:absolute;top:10px;display:flex;align-items:center;gap:6px}
.topbar b{font-weight:600}
.auth{position:absolute;left:854px;top:6px;width:120px;height:22px;background:#fff;border-radius:11px;display:flex;font-size:8px;font-weight:600;color:#111}
.auth span{flex:1;display:flex;align-items:center;justify-content:center}
.auth span+span{border-left:1px solid #ccc}
.header{left:0;top:33px;width:1200px;height:89px;background:#fff}
.brand{position:absolute;left:14px;top:14px;display:flex;align-items:center;gap:8px}
.brand .mark{width:46px;height:46px;border-radius:50%;background:var(--blue)}
.brand .name{font-size:22px;font-weight:500;color:var(--blue);line-height:1;letter-spacing:1px}
.brand .sub{font-size:8px;color:var(--blue);letter-spacing:2px;font-weight:500}
.nav{position:absolute;left:300px;top:36px;display:flex;gap:30px;font-size:13px;color:#222}
.nav .active{color:var(--blue);position:relative}
.nav .active:after{content:"";position:absolute;left:-4px;right:-4px;top:50px;height:3px;background:var(--blue)}
.btn-contact{position:absolute;left:839px;top:23px;width:128px;height:41px;background:var(--blue);color:#fff;font-size:13px;font-weight:600;display:flex;align-items:center;justify-content:center}
.callbox{left:1000px;top:0;width:188px;height:108px;border:8px solid var(--blue);border-top:none;background:#fff;padding:16px 0 0 14px}
.callbox .row{display:flex;align-items:center;gap:10px;color:var(--blue);font-size:14px}
.callbox .ico{width:34px;height:34px;background:var(--blue);border-radius:4px;display:flex;align-items:center;justify-content:center}
.callbox .num{margin-top:14px;font-size:15px;font-weight:600;color:var(--blue)}
.hero{left:0;top:122px;width:1200px;height:510px;background:radial-gradient(ellipse at 65% 40%,#2a2f8e 0%,#171d6a 45%,#0c1450 100%)}
.hero-photo{left:218px;top:115px;width:357px;height:280px;border-radius:6px;background:linear-gradient(135deg,#d9dce0,#aab1ba 60%,#6a7686)}
.hero-text{left:621px;top:140px;width:440px;color:#fff}
.hero-text .eyebrow{font-size:14px;font-weight:600}
.hero-text h1{font-size:47px;font-weight:800;line-height:45px;margin-top:16px;letter-spacing:-.5px}
.hero-text p{font-size:12.5px;line-height:18px;margin-top:24px}
.hero-text .btn{display:inline-flex;margin-top:14px;width:128px;height:41px;background:#fff;color:var(--blue);font-size:13px;font-weight:600;align-items:center;justify-content:center;border-radius:2px}
.arrow{top:194px;width:43px;height:75px;display:flex;align-items:center;justify-content:center}
.arrow.left{left:0;border:1px solid #fff;border-left:none;background:transparent}
.arrow.right{left:1157px;background:#3b7fd4}
.partners{left:0;top:632px;width:1200px;height:139px;background:var(--grey-bg)}
.partners .p{position:absolute;top:61px;display:flex;align-items:center;gap:8px;color:#9a9a9a;font-size:13px;font-weight:600}
.partners .p i{width:22px;height:22px;border-radius:50%;background:#b9b9b9;display:block}
.eyebrow-dark{font-size:14px;color:#222}
h2{font-size:28px;font-weight:700;color:var(--ink);line-height:33px}
.services{left:0;top:771px;width:1200px;height:501px;background:#fff}
.card{position:absolute;top:173px;width:428px;height:274px;padding:32px 32px}
.card h3{font-size:21px;font-weight:500;margin-top:20px}
.card p{font-size:12.5px;line-height:22.5px;margin-top:18px}
.card a{display:inline-block;margin-top:10px;font-size:12.5px;text-decoration:underline;color:inherit}
.card.primary{left:161px;background:var(--blue);color:#fff}
.card.plain{left:612px;border:1px solid #e3e3ea;color:#222}
.about{left:0;top:1272px;width:1200px;height:564px;background:var(--grey-bg)}
.about p{font-size:12.5px;line-height:22.5px;color:#222}
.photo{background:linear-gradient(135deg,#c9b79a,#7e6d5a 55%,#3d3a3a)}
.btn-blue{background:var(--blue);color:#fff;font-size:12px;display:flex;align-items:center;justify-content:center}
.clients{left:0;top:1836px;width:1200px;height:600px;background:#fff}
.map{left:130px;top:45px;width:950px;height:520px;background:radial-gradient(ellipse at center,#f1f2f6 0%,#f7f8fa 55%,#fff 75%)}
.dot{position:absolute;border-radius:50%;background:#cfe6fb}
.dot:after{content:"";position:absolute;left:50%;top:50%;width:9px;height:9px;margin:-4.5px 0 0 -4.5px;border-radius:50%;background:#2c9af0}
.tcard{position:absolute;top:219px;width:377px;height:253px;background:#fff;box-shadow:0 4px 22px rgba(0,0,0,.08);padding:38px 36px}
.tcard .head{display:flex;align-items:center;gap:22px;margin-left:-7px}
.tcard .av{width:66px;height:66px;border-radius:50%;background:#f1f3f7;display:flex;align-items:center;justify-content:center}
.tcard .av i{width:28px;height:28px;border-radius:50%;background:var(--blue);display:block}
.tcard h4{font-size:16px;font-weight:600;color:#222}
.tcard small{font-size:11px;color:var(--muted)}
.tcard p{font-size:12.5px;line-height:22.5px;color:#222;margin-top:26px}
.footer{left:0;top:2436px;width:1200px;height:350px;background:var(--footer);color:#fff}
.footer h5{font-size:21px;font-weight:600}
.footer .lorem{font-size:11.5px;line-height:22.5px}
.links{list-style:none;font-size:11.5px;font-weight:600}
.links li{height:27px;display:flex;align-items:center;gap:10px}
.links li:before{content:"···";letter-spacing:1px}
.newsletter{left:714px;top:72px;width:381px;height:230px;background:var(--news);text-align:center;padding-top:40px}
.newsletter h6{font-size:21px;font-weight:600}
.newsletter p{font-size:11.5px;line-height:22.5px;margin:10px 24px 0}
.sub-form{position:absolute;left:40px;top:161px;width:310px;height:33px;background:#fff;border-radius:17px;font-size:11px;color:#9bb8d6;display:flex;align-items:center;padding-left:25px}
.sub-form span{position:absolute;right:2px;top:2px;width:106px;height:29px;border-radius:15px;background:var(--blue);color:#fff;display:flex;align-items:center;justify-content:center}
.bottombar{left:0;top:2786px;width:1200px;height:76px;background:var(--blue);color:#fff;font-size:9px}
.social{position:absolute;top:28px;width:23px;height:23px;border-radius:50%;border:2px solid #fff}
</style>
</head>
<body>

<div class="abs topbar">
  <div class="item" style="left:20px"><svg width="14" height="12"><rect x="1" y="2" width="12" height="8" rx="2" fill="none" stroke="#fff"/></svg><span><b>Need Help?</b> Call Us! <b>(800) 555-0147</b></span></div>
  <div class="item" style="left:299px"><svg width="16" height="12"><rect x="1" y="1" width="14" height="10" fill="none" stroke="#fff"/><path d="M1 1l7 6 7-6" fill="none" stroke="#fff"/></svg><span><b>Email:</b> sales@brindlewave.example</span></div>
  <div class="item" style="left:556px"><svg width="13" height="13"><circle cx="6.5" cy="6.5" r="5.5" fill="none" stroke="#fff"/><path d="M6.5 3v4h3" fill="none" stroke="#fff"/></svg><span>Mon - Fri: 7:30am - 3:30pm, Sat - Sun: <b>CLOSED PST</b></span></div>
  <div class="auth"><span>LOGIN</span><span>REGISTER</span></div>
</div>

<div class="abs header">
  <div class="brand"><div class="mark"></div><div><div class="name">VELLORA</div><div class="sub">CONSULTING</div></div></div>
  <nav class="nav"><span class="active">Home</span><span>Services ⌄</span><span>Why Vellora?</span><span>Vellora Leadership</span><span>Contact Us</span></nav>
  <div class="btn-contact">CONTACT US</div>
</div>

<div class="abs callbox">
  <div class="row"><div class="ico"><svg width="16" height="16" viewBox="0 0 24 24"><path fill="#fff" d="M6.6 10.8a15 15 0 006.6 6.6l2.2-2.2a1 1 0 011-.25 11.4 11.4 0 003.6.57 1 1 0 011 1V20a1 1 0 01-1 1A17 17 0 013 4a1 1 0 011-1h3.5a1 1 0 011 1c0 1.25.2 2.45.57 3.57a1 1 0 01-.25 1z"/></svg></div>Call Us For Free</div>
  <div class="num">+1-800-555-0192</div>
</div>

<section class="abs hero">
  <div class="abs hero-photo" role="img" aria-label="Photo of two colleagues reviewing charts on a laptop"></div>
  <div class="abs hero-text">
    <div class="eyebrow">// Only High-Quality Services</div>
    <h1>SOFTWARE IT<br>OUTSOURCING</h1>
    <p>At Vellora, we are proud to have a team of seasoned IT professionals who understand what it takes to deliver a quality solution.</p>
    <div class="btn">LEARN MORE</div>
  </div>
  <div class="abs arrow left"><svg width="20" height="14"><path d="M19 7H2M8 1L2 7l6 6" fill="none" stroke="#fff" stroke-width="2"/></svg></div>
  <div class="abs arrow right"><svg width="20" height="14"><path d="M1 7h17M12 1l6 6-6 6" fill="none" stroke="#fff" stroke-width="2"/></svg></div>
</section>

<section class="abs partners">
  <div class="p" style="left:168px"><i></i>Pellix</div>
  <div class="p" style="left:310px"><i></i>Northpeak</div>
  <div class="p" style="left:467px"><i></i>Quillora</div>
  <div class="p" style="left:623px"><i></i>Tandemly</div>
  <div class="p" style="left:779px"><i></i>Orbital Co</div>
  <div class="p" style="left:936px"><i></i>Fernhost</div>
</section>

<section class="abs services">
  <div class="abs eyebrow-dark" style="left:164px;top:48px">// Our Services</div>
  <h2 class="abs" style="left:164px;top:83px">We Offer a Wide<br>Variety of IT Services</h2>
  <div class="card primary">
    <svg width="50" height="50" viewBox="0 0 50 50"><circle cx="25" cy="25" r="8" fill="none" stroke="#fff" stroke-width="3"/><circle cx="25" cy="25" r="3" fill="#fff"/><g stroke="#fff" stroke-width="3"><path d="M25 2v10M25 38v10M2 25h10M38 25h10M9 9l7 7M34 34l7 7M41 9l-7 7M16 34l-7 7"/></g></svg>
    <h3>Custom Solution Delivery</h3>
    <p>Vellora offers a range of services focused on helping businesses and organizations deliver software solutions to their customers or users.</p>
    <a>Read More</a>
  </div>
  <div class="card plain">
    <svg width="50" height="50" viewBox="0 0 50 50"><g fill="none" stroke="#1a62b4" stroke-width="2.5"><path d="M10 4v16M25 4v16M40 4v16M6 8l4-4 4 4M21 8l4-4 4 4M36 8l4-4 4 4"/><circle cx="25" cy="28" r="5"/></g><path d="M4 44c0-6 4-10 8-10s8 4 8 10zM30 44c0-6 4-10 8-10s8 4 8 10zM16 46c0-6 4-10 9-10s9 4 9 10z" fill="#1a62b4"/></svg>
    <h3>Staff Augmentation</h3>
    <p>Let Vellora help you supplement your existing software development teams with additional resources and expertise. We provided access to experienced</p>
    <a>Read More</a>
  </div>
</section>

<section class="abs about">
  <div class="abs eyebrow-dark" style="left:164px;top:53px">// About Our Company</div>
  <h2 class="abs" style="left:164px;top:88px">Consultancy<br>Industries</h2>
  <p class="abs" style="left:164px;top:183px;width:430px">Welcome to Vellora, a software consulting company specializing in serving small to medium size businesses. We understand the unique challenges and opportunities that these companies face, and we are dedicated to helping them succeed through innovative technology solutions.</p>
  <p class="abs" style="left:164px;top:318px;width:430px">Our team of experienced professionals has a diverse range of skills and expertise, making us well-equipped to handle any project, big or small. We specialize in custom software development, working closely with our clients to understand their specific needs and build solutions that meet their requirements.</p>
  <div class="abs btn-blue" style="left:163px;top:455px;width:187px;height:41px">LEANR MORE ABOUT US</div>
  <div class="abs photo" style="left:612px;top:98px;width:427px;height:302px" role="img" aria-label="Photo of a team meeting in a bright lounge"></div>
  <div class="abs photo" style="left:1095px;top:201px;width:105px;height:142px;background:linear-gradient(135deg,#e9ecef,#b7bcc4 60%,#5d6570)" role="img" aria-label="Photo of colleagues talking in an office"></div>
  <div class="abs photo" style="left:959px;top:323px;width:196px;height:155px;background:linear-gradient(135deg,#d8c3a1,#8e7457 55%,#3f3a38)" role="img" aria-label="Overhead photo of a team working around a desk"></div>
</section>

<section class="abs clients">
  <div class="abs map" role="img" aria-label="Faint world map background"></div>
  <div class="dot" style="left:199px;top:161px;width:43px;height:43px"></div>
  <div class="dot" style="left:312px;top:129px;width:22px;height:22px"></div>
  <div class="dot" style="left:748px;top:97px;width:25px;height:25px;background:none"></div>
  <div class="dot" style="left:888px;top:121px;width:40px;height:40px"></div>
  <div class="dot" style="left:1014px;top:185px;width:20px;height:20px"></div>
  <div class="dot" style="left:657px;top:476px;width:36px;height:36px"></div>
  <div class="dot" style="left:379px;top:497px;width:25px;height:25px"></div>
  <div class="abs eyebrow-dark" style="left:575px;top:85px">// Our Clients</div>
  <h2 class="abs" style="left:0;width:1240px;text-align:center;top:113px;font-size:28px">ConsultaWe are Trusted<br>15+ Countries Worldwide</h2>
  <div class="tcard" style="left:200px">
    <div class="head"><div class="av"><i></i></div><div><h4>Harlow Works LTD,</h4><small>Client of Company</small></div></div>
    <p>Suspendisse potenti. Nunc ac vulputate odio. Morbi vel libero dui. Duis sollicitudin purus vel facilisis feugiat. Duis sit amet laoreet leo. Donec id tempor augue, ac tincidunt tellus. Ut vitae rutrum mi.</p>
  </div>
  <div class="tcard" style="left:625px">
    <div class="head"><div class="av"><i></i></div><div><h4>Corbyn Labs,</h4><small>Manager of Company</small></div></div>
    <p>Morbi fringilla eleifend ultricies. Nunc dapibus sit amet quam ut lacinia. Class aptent taciti sociosqu ad litora torquent per conubia nostra, per inceptos himenaeos. Morbi sollicitudin at nulla at fermentum.</p>
  </div>
</section>

<footer class="abs footer">
  <h5 class="abs" style="left:162px;top:66px">Company</h5>
  <p class="abs lorem" style="left:162px;top:127px;width:230px">Lorem ipsum dolor sit amet, consectetur adipiscing elit. Nulla non ante nec arcu tempor tempus. Sed venenatis nibh vitae lacus faucibus, et tristique sem ornare.</p>
  <h5 class="abs" style="left:493px;top:66px">Page Link</h5>
  <ul class="abs links" style="left:493px;top:125px"><li>Home</li><li>Services</li><li>Why Vellora?</li><li>Vellora Leadership</li><li>Contact Us</li></ul>
  <div class="abs newsletter">
    <h6>Newsletter</h6>
    <p>Subscribe to out newsletter today to receive updates on the latest news, releases and special offers. We respect your privacy. Your information is safe.</p>
    <div class="sub-form">Your Email address<span>Subscribe</span></div>
  </div>
</footer>

<div class="abs bottombar">
  <div class="abs" style="left:162px;top:35px">© Copyright 2022 brindlewave. All Rights Reserved.</div>
  <div class="social" style="left:1003px" aria-label="Social link"></div>
  <div class="social" style="left:1037px" aria-label="Social link"></div>
  <div class="social" style="left:1071px" aria-label="Social link"></div>
</div>

</body>
</html>
```